Logo + Business Card Design Project

We are looking at changing our logo and reprinting business cards.

Attached is a design concept for the logo (we have no hi res files for this).

The logo needs to be able to work standalone without the tagline.

We are happy for you to use this concept or design a new one. The existing concept is quite well liked.

We would also consider not having Solutions in the logo and just have QRV Systems Pty Ltd in the body text of the card.

We have a Tag Line that needs to go on all documentation / websites etc wherever the logo appears.

Tagline: Turning IT up

Our message to clients is that we have solutions that:

QRV Systems:
Turning IT up

Turning up Revenue
Turning up Profit
Turning up Confidence

We would require the files in a High Res format for print and a scalable transparent format for web.
(We also need greyscale and monochrome files)
All source files need to be delivered with existing layers etc

A corporate guide with the logo usage and colours should be specified.

Suggestions:
The new logo has to have CMYK colours of 100 90 0 0

CMYK 100 90 0 0
RGB #21409A
Websafe #224499
Greyscale #414141

We would also need a business card layout designed.
Could be one sided or 2 sided. Will probably print matt cello 2 sides on 350gsm gloss
Updates

Industry/Entity Type

Business

Requirements
Should not have
• Lower case n in QRV.

```html
<!DOCTYPE html>
<html lang="en">
<head>
<meta charset="utf-8">
<title>QRV Systems – Business Card</title>
<link rel="stylesheet" href="https://fonts.googleapis.com/css2?family=Cinzel:wght@500&family=Cormorant+Garamond:wght@500&family=Great+Vibes&display=swap">
<style>
  :root {
    --card-red: #d0020e;
    --gold: #c9952f;
    --gold-soft: #b8922c;
    --brand-blue: #21409a;
  }
  html, body {
    margin: 0;
    padding: 0;
    width: 1200px;
    height: 848px;
    overflow: hidden;
    background: var(--card-red);
  }
  .card {
    position: relative;
    width: 1200px;
    height: 848px;
    background: var(--card-red);
  }
  .brand {
    position: absolute;
    top: 84px;
    left: 0;
    width: 1200px;
    display: flex;
    flex-direction: column;
    align-items: center;
  }
  .brand-lockup {
    display: flex;
    align-items: center;
    gap: 28px;
  }
  .brand-disc {
    width: 150px;
    height: 150px;
    display: block;
  }
  .brand-name {
    font-family: "Cinzel", serif;
    font-weight: 500;
    font-size: 66px;
    color: var(--gold);
    letter-spacing: 2px;
    line-height: 1;
  }
  .brand-tagline {
    margin: 16px 0 0 0;
    font-family: "Cormorant Garamond", serif;
    font-weight: 500;
    font-size: 30px;
    letter-spacing: 3px;
    color: var(--gold);
    line-height: 1;
  }
  .holder {
    position: absolute;
    top: 360px;
    left: 0;
    width: 1200px;
    text-align center;
    text-align: center;
  }
  .holder-name {
    margin: 0;
    font-family: "Cinzel", serif;
    font-weight: 500;
    font-size: 52px;
    letter-spacing: 2px;
    color: var(--gold);
    line-height: 1;
  }
  .holder-title {
    margin: 0;
    font-family: "Great Vibes", cursive;
    font-size: 70px;
    color: var(--gold);
    line-height: 1;
  }
  .contact {
    position: absolute;
    top: 538px;
    margin: 0;
    font-family: "Cormorant Garamond", serif;
    font-weight: 500;
    font-size: 30px;
    line-height: 43px;
    font-variant-numeric: lining-nums;
    color: var(--gold-soft);
  }
  .contact-phone { left: 97px; }
  .contact-online { left: 583px; }
  .contact dt, .contact dd { display: inline; margin: 0; }
  .contact .row { display: block; white-space: nowrap; }
  .contact .indent { padding-left: 130px; }
</style>
</head>
<body>
<main class="card">
  <header class="brand">
    <div class="brand-lockup">
      <svg class="brand-disc" viewBox="0 0 150 150" aria-hidden="true">
        <circle cx="75" cy="75" r="75" fill="var(--brand-blue)"/>
      </svg>
      <span class="brand-name">QRV Systems</span>
    </div>
    <p class="brand-tagline">Turning IT up</p>
  </header>

  <section class="holder">
    <h1 class="holder-name">Daniel Whitcombe</h1>
    <p class="holder-title">Project Director</p>
  </section>

  <dl class="contact contact-phone">
    <div class="row"><dt>Phone:</dt> <dd>+ 61 2 9518-4200</dd></div>
    <div class="row"><dt>Support:</dt> <dd>+ 61 2 9518-4233</dd></div>
    <div class="row"><dt>Fax:</dt> <dd>+ 61 2 9518-4201</dd></div>
    <div class="row"><dt>Mobile:</dt> <dd>0400 582 193</dd></div>
  </dl>

  <dl class="contact contact-online">
    <div class="row"><dt>Email:</dt> <dd>daniel.whitcombe@qrv.com.au</dd></div>
    <div class="row"><dt>Web:</dt> <dd>&nbsp;www.qrv.com.au</dd></div>
    <div class="row"><dt>Address:</dt> <dd>318/42 Belmore Street</dd></div>
    <div class="row indent"><dd>Crows Nest NSW&nbsp; 2071</dd></div>
  </dl>
</main>
</body>
</html>
```